Global Expert Network Firm needs business card design

We need business card design for a new company based in Seoul, South Korea called 'Corwell Insight Partners'. We recruit industry experts covering all countries and connect our client and recruited expert by phone, face-to-face meetings and etc. We are a global expert network firm that is focused on delivering high-quality experts to our clients throughout the world. Our clients include multinational corporations, global consulting firms, private equity firms, venture capital firms, asset management companies.
We have made new logo and please find attachment.(Please use new logo)
Target Market(s)
Global Consulting Firms, Investment Firms, Private Equity Firms, Venture Capital Firms.
Industry/Entity Type
Recruitment
Contact Information for Business Card
We need two Languages (English and Korean Version).
The front is Korean and the back is English version.
[The back] [English]
Company Name: Corwell Insight Partners, Inc.
CEO Name: Derek Hwang
Address: #508, Daerim Bldg, 72 Mokdongseo-ro, Yangcheon-gu, Seoul, 07918, Korea
Tel. +82 2 847 1215
Fax. +82 2 761 4218
Mobile. +82 10 6284 1215
Email: derek@corwellip.com
Web: www.corwellip.com
[The front] [Korean] => Described in same order as English version.
회사명: 코웰인사이트파트너스(주)
대표이사: 황도윤
주소: 서울시 양천구 목동서로 72 대림빌딩 508호
Tel. 02 847 1215
Fax. 02 761 4218
Mobile. 010 6284 1215
Web: www.corwellip.com

```html
<!DOCTYPE html>
<html lang="en">
<head>
<meta charset="utf-8">
<title>Corwell Insight Partners — Business Cards</title>
<link href="https://fonts.googleapis.com/css2?family=Mulish:wght@400;700&family=Noto+Sans+KR:wght@300;400&display=swap" rel="stylesheet">
<style>
  :root {
    --bg: #d9d9d9;
    --card: #e4e4e4;
    --navy: #1b2049;
    --ink: #1b2049;
    --muted: #8b8b8b;
    --paper-text: #ffffff;
  }
  * { box-sizing: border-box; margin: 0; padding: 0; }
  html, body { width: 1200px; height: 965px; overflow: hidden; }
  body {
    background: var(--bg);
    font-family: "Mulish", sans-serif;
    position: relative;
  }
  .card {
    position: absolute;
    left: 277px;
    width: 648px;
    height: 370px;
    background: var(--card);
  }
  .card--en { top: 97px; }
  .card--ko { top: 502px; }

  .identity { position: absolute; left: 29px; top: 48px; color: var(--ink); }
  .identity__name { font-weight: 700; font-size: 26px; line-height: 1.1; }
  .identity__title { font-size: 16px; line-height: 1.2; }
  .card--ko .identity { left: 30px; top: 44px; }
  .card--ko .identity__name {
    font-family: "Noto Sans KR", sans-serif; font-weight: 400;
    font-size: 29px; letter-spacing: 2px;
  }
  .card--ko .identity__title {
    font-family: "Noto Sans KR", sans-serif; font-weight: 300;
    font-size: 19px; color: var(--muted); letter-spacing: 2px; margin-top: 1px;
  }

  .band { position: absolute; top: 132px; height: 207px; background: var(--navy); }
  .band--info { left: 0; width: 400px; }
  .band--mark { left: 408px; width: 201px; }
  .band--edge { left: 617px; width: 31px; }

  .contact { position: absolute; left: 30px; top: 20px; color: var(--paper-text); font-size: 15px; }
  .contact__address { line-height: 18.5px; }
  .card--ko .contact__address {
    font-family: "Noto Sans KR", sans-serif; font-weight: 300;
    letter-spacing: 1px; line-height: 19px; margin-left: -1px;
  }
  .contact__list { list-style: none; margin-top: 18px; }
  .card--ko .contact__list { margin-top: 20px; }
  .contact__list li { display: flex; align-items: center; height: 19.6px; }
  .contact__list svg {
    width: 12px; height: 12px; margin-right: 7px; flex: none;
    fill: none; stroke: var(--paper-text); stroke-width: 1.2;
  }

  .company {
    position: absolute; left: 10px; top: 30px; right: 10px;
    color: var(--paper-text); font-weight: 400; font-size: 30px;
    line-height: 56px; text-transform: uppercase; letter-spacing: 0.5px;
  }
</style>
</head>
<body>

<svg width="0" height="0" style="position:absolute">
  <defs>
    <symbol id="icon-mobile" viewBox="0 0 12 12"><rect x="3" y="1" width="6" height="10" rx="1"/></symbol>
    <symbol id="icon-phone" viewBox="0 0 12 12"><path d="M2 2.5 4 1.5 5.5 4 4.5 5a5 5 0 0 0 2.5 2.5l1-1 2.5 1.5-1 2C5 10 2 7 2 2.5Z"/></symbol>
    <symbol id="icon-fax" viewBox="0 0 12 12"><rect x="3" y="1" width="6" height="3"/><rect x="1" y="4" width="10" height="5"/><rect x="3" y="7" width="6" height="4"/></symbol>
    <symbol id="icon-mail" viewBox="0 0 12 12"><rect x="1" y="2.5" width="10" height="7"/><path d="M1 2.5 6 7l5-4.5M1 9.5l4-3.5m6 3.5-4-3.5"/></symbol>
    <symbol id="icon-web" viewBox="0 0 12 12"><circle cx="6" cy="6" r="5"/><ellipse cx="6" cy="6" rx="2.2" ry="5"/><path d="M1 6h10M2 3.5h8M2 8.5h8"/></symbol>
  </defs>
</svg>

<section class="card card--en" lang="en">
  <div class="identity">
    <h1 class="identity__name">DEREK HWANG</h1>
    <p class="identity__title">CEO</p>
  </div>
  <div class="band band--info">
    <div class="contact">
      <p class="contact__address">#508, Daerim Bldg,<br>72 Mokdongseo-ro, Yangcheon-gu,<br>Seoul, 07918, Korea</p>
      <ul class="contact__list">
        <li><svg><use href="#icon-mobile"/></svg>+82 2 847 1215</li>
        <li><svg><use href="#icon-phone"/></svg>+82 2 761 4218</li>
        <li><svg><use href="#icon-fax"/></svg>+82 10 6284 1215</li>
        <li><svg><use href="#icon-mail"/></svg>derek@corwellip.com</li>
        <li><svg><use href="#icon-web"/></svg>www.corwellip.com</li>
      </ul>
    </div>
  </div>
  <div class="band band--mark"><p class="company">Corwell<br>Insight<br>Partners</p></div>
  <div class="band band--edge"></div>
</section>

<section class="card card--ko" lang="ko">
  <div class="identity">
    <h2 class="identity__name">황도윤</h2>
    <p class="identity__title">대표이사</p>
  </div>
  <div class="band band--info">
    <div class="contact">
      <p class="contact__address">서울시 양천구 목동서로<br>72 대림빌딩 508호</p>
      <ul class="contact__list">
        <li><svg><use href="#icon-mobile"/></svg>+82 2 847 1215</li>
        <li><svg><use href="#icon-phone"/></svg>+82 2 761 4218</li>
        <li><svg><use href="#icon-fax"/></svg>+82 10 6284 1215</li>
        <li><svg><use href="#icon-mail"/></svg>derek@corwellip.com</li>
        <li><svg><use href="#icon-web"/></svg>www.corwellip.com</li>
      </ul>
    </div>
  </div>
  <div class="band band--mark"><p class="company">Corwell<br>Insight<br>Partners</p></div>
  <div class="band band--edge"></div>
</section>

</body>
</html>
```